Package design for quilted mattress covers.

We are producing a comfortable "quilted mattress protector" for beds . We need a very elegant and attractive and cozy insert label. approx. size is 14 inches high x11 inches wide. (One base design with slight edits to customize for each different bed size) It will be packaged in a nice clear bag, with the design label in front. I attached the type of product for reference

package text:
QUILTED MATTRESS COVER

size: 33x75x10"

*ultimate comfort
*breathable cotton top
*waterproof lining
*easy care wash and dry
Updates

Target Market(s)

displayed in drygood and bedding retail stores

Colors

Designer to choose colors to be used in the design.

Requirements
Must have
• all info as in description
Nice to have
• an image of a quilted cover on a bed, professionally included in the package design
Should not have
• ..

```html
<!DOCTYPE html>
<html lang="en">
<head>
<meta charset="UTF-8">
<title>Calmwell Quilted Mattress Cover – Package Insert</title>
<link href="https://fonts.googleapis.com/css2?family=Barlow+Semi+Condensed:wght@500;600&family=Barlow:wght@500;700&display=swap" rel="stylesheet">
<style>
  :root{
    --page:#e6e8ea;
    --sky:#29abe2;
    --band:#3d5a8a;
    --paper:#ffffff;
    --size-light:#6090cf;
    --navy:#120f2b;
    --title:#3d5a8a;
    --photo-top:#eef0f3;
    --photo-bottom:#d4d8de;
  }
  html,body{margin:0;padding:0;width:1200px;height:1200px;overflow:hidden;background:var(--page);}
  .canvas{position:relative;width:1200px;height:1200px;}
  .label{position:absolute;left:156px;top:36px;width:887px;height:1129px;}
  .label > *{position:absolute;left:0;width:100%;}
  .hero{top:0;height:329px;background:var(--sky);display:flex;align-items:center;justify-content:center;}
  .brand-name{font-family:"Barlow",sans-serif;font-weight:700;font-size:84px;color:var(--paper);letter-spacing:-1px;margin:0;}
  .band{height:40px;background:var(--band);}
  .band--upper{top:329px;}
  .band--lower{top:456px;}
  .title-strip{top:369px;height:87px;background:var(--paper);display:flex;align-items:center;justify-content:center;}
  .product-title{font-family:"Barlow Semi Condensed",sans-serif;font-weight:500;font-size:50px;color:var(--title);margin:0;}
  .product-photo{top:496px;height:421px;background:linear-gradient(180deg,var(--photo-top) 0%,var(--photo-bottom) 100%);}
  .info-bar{top:917px;height:212px;background:var(--navy);}
  .size-box{position:absolute;left:0;top:0;width:225px;height:212px;}
  .size-heading{height:106px;background:var(--size-light);display:flex;align-items:center;justify-content:center;font-family:"Barlow",sans-serif;font-weight:500;font-size:34px;letter-spacing:17px;color:var(--paper);padding-left:17px;box-sizing:border-box;}
  .size-value{height:106px;background:var(--band);display:flex;align-items:center;justify-content:center;font-family:"Barlow",sans-serif;font-weight:500;font-size:30px;color:var(--paper);}
  .features{position:absolute;left:225px;top:0;right:0;height:212px;}
  .feature{position:absolute;top:45px;width:130px;margin-left:-65px;text-align:center;}
  .feature svg{display:block;margin:0 auto;width:78px;height:78px;}
  .feature-text{margin-top:22px;font-family:"Barlow",sans-serif;font-weight:500;font-size:15px;line-height:19px;color:var(--paper);}
</style>
</head>
<body>
<div class="canvas">
  <div class="label">
    <header class="hero"><p class="brand-name">Calmwell</p></header>
    <div class="band band--upper"></div>
    <div class="title-strip"><h1 class="product-title">Quilted Mattress Cover</h1></div>
    <div class="band band--lower"></div>
    <div class="product-photo" role="img" aria-label="Photo of a white quilted mattress cover on a bed with pillows in a bright bedroom"></div>
    <section class="info-bar">
      <div class="size-box">
        <div class="size-heading">SIZE</div>
        <div class="size-value">33x75x10”</div>
      </div>
      <div class="features">
        <div class="feature" style="left:122px">
          <svg viewBox="0 0 80 80"><circle cx="40" cy="40" r="39" fill="#fff"/>
            <path d="M54 22c-14 2-24 14-24 26l-4 12M54 22c2 12-8 26-24 26" fill="none" stroke="#120f2b" stroke-width="3" stroke-linecap="round"/></svg>
          <div class="feature-text">Ultimate<br>Comfort</div>
        </div>
        <div class="feature" style="left:260px">
          <svg viewBox="0 0 80 80"><circle cx="40" cy="40" r="39" fill="#fff"/>
            <g fill="none" stroke="#120f2b" stroke-width="2.5" stroke-linecap="round">
              <path d="M20 40q20-10 40 0q-20 10-40 0"/>
              <path d="M40 30V16M35 21l5-5 5 5M40 50v14M35 59l5 5 5-5M28 30l-6-8M52 30l6-8M28 50l-6 8M52 50l6 8"/></g></svg>
          <div class="feature-text">Breathable<br>Cotton Top</div>
        </div>
        <div class="feature" style="left:398px">
          <svg viewBox="0 0 80 80"><circle cx="40" cy="40" r="39" fill="#fff"/>
            <path d="M34 20c-8 12-12 18-12 24a12 12 0 0 0 24 0c0-6-4-12-12-24z" fill="none" stroke="#120f2b" stroke-width="3"/>
            <path d="M52 34c-5 7-7 11-7 14a7 7 0 0 0 14 0c0-3-2-7-7-14z" fill="#120f2b"/></svg>
          <div class="feature-text">Waterproof<br>Lining</div>
        </div>
        <div class="feature" style="left:536px">
          <svg viewBox="0 0 80 80"><circle cx="40" cy="40" r="39" fill="#fff"/>
            <path d="M20 30l5 22h30l5-22M20 30q5 4 10 0t10 0 10 0 10 0" fill="none" stroke="#120f2b" stroke-width="3" stroke-linejoin="round"/>
            <path d="M40 46l-6-6a3.5 3.5 0 0 1 6-4 3.5 3.5 0 0 1 6 4z" fill="#120f2b"/></svg>
          <div class="feature-text">Easy Care Wash<br>And Dry</div>
        </div>
      </div>
    </section>
  </div>
</div>
</body>
</html>
```